Plumbing & Heating bussiness card design

i do all plumbing and heating work and need a catchy design. keep it simple but eye catching nothing gimicky
i do 24hr call outs
landlord safety checks
all aspects of plumbing and heating
boiler breakdowns
flue sure reg number 804617
i have put up my old card. not to bothered about the front but i have put up the back for the details. mobile number and office are the same and the email has changed to tolwenpipes@mailvoro.net

Industry/Entity Type

Safety

Contact Information for Business Card

i do 24hr call outs
landlord safety checks
boiler breakdowns

Requirements
Must have
• i do 24hr call outs
• landlord safety checks
• all aspects of plumbing and heating
• boiler breakdowns
• flue sure reg number 804617

```html
<!DOCTYPE html>
<html lang="en">
<head>
<meta charset="utf-8">
<title>T Olwen Plumbing &amp; Heating – Business Card</title>
<link href="https://fonts.googleapis.com/css2?family=Open+Sans:wght@400;600;700&family=Michroma&display=swap" rel="stylesheet">
<style>
  :root {
    --backdrop: #2b2b2c;
    --card-grey: #58585a;
    --brand-red: #be1e2d;
    --label-red: #d4283a;
    --services-yellow: #f7d100;
    --badge-neutral: #e6e6e6;
    --text-white: #ffffff;
    --brand-blue: #2b8fdc;
  }
  * { box-sizing: border-box; margin: 0; padding: 0; }
  html, body {
    width: 1200px; height: 799px; overflow: hidden;
    background: var(--backdrop);
    font-family: "Open Sans", Arial, sans-serif;
  }
  .canvas { position: relative; width: 1200px; height: 799px; }

  .card {
    position: absolute;
    width: 520px; height: 300px;
    background: var(--card-grey);
    box-shadow: 0 10px 28px rgba(0,0,0,.45);
    overflow: hidden;
  }
  .card--details { left: 80px; top: 80px; }
  .card--brand { left: 600px; top: 420px; }

  /* details side */
  .holder-name {
    position: absolute; left: 38px; top: 70px;
    font-family: "Michroma", "Open Sans", sans-serif;
    font-size: 40px; font-weight: 400; color: var(--text-white); letter-spacing: 1px;
  }
  .contact-list {
    position: absolute; left: 38px; top: 168px;
    list-style: none; font-size: 14px; line-height: 25px; color: var(--text-white);
  }
  .contact-list .label { color: var(--label-red); display: inline-block; width: 62px; }
  .contact-list .address { margin-top: 4px; font-size: 15px; }

  .services-panel {
    position: absolute; right: 0; top: 0;
    width: 250px; height: 232px;
    background: var(--brand-red);
    border-bottom-left-radius: 46px;
    padding: 34px 0 0 24px;
    color: var(--text-white);
  }
  .services-title {
    font-size: 20px; font-weight: 700; color: var(--services-yellow);
    margin-bottom: 8px;
  }
  .services-list { list-style: none; font-size: 11.5px; font-weight: 600; line-height: 27px; }
  .services-list li::before { content: "- "; }
  .register-badge {
    position: absolute; right: 20px; top: 14px;
    width: 56px; height: 52px;
    background: var(--badge-neutral);
    border-radius: 4px;
  }

  /* brand side */
  .brand-lockup {
    position: absolute; left: 0; right: 0; top: 118px;
    display: flex; align-items: center; justify-content: center; gap: 14px;
  }
  .brand-dot { width: 26px; height: 26px; border-radius: 50%; background: var(--brand-red); }
  .brand-name {
    font-family: "Open Sans", Arial, sans-serif;
    font-weight: 700; font-size: 28px; letter-spacing: 1px;
    color: var(--brand-blue); text-transform: uppercase; line-height: 1.15;
    text-align: center;
  }
</style>
</head>
<body>
<main class="canvas">

  <section class="card card--details">
    <h1 class="holder-name">Tom</h1>
    <ul class="contact-list">
      <li><span class="label">Mobile :</span>07700 900418</li>
      <li><span class="label">Office :</span>01632 960 275</li>
      <li><span class="label">E-mail :</span>tolwenpipes@mailvoro.net</li>
      <li class="address">14 Carrow Lane, Treloweth, TR9 4QB</li>
    </ul>

    <div class="services-panel">
      <div class="register-badge" role="img" aria-label="Registration badge placeholder"></div>
      <h2 class="services-title">Services:</h2>
      <ul class="services-list">
        <li>I do 24hr call outs</li>
        <li>Landlord safety checks</li>
        <li>All aspects of plumbing and heating</li>
        <li>Boiler breakdowns</li>
        <li>Flue sure reg number 804617</li>
      </ul>
    </div>
  </section>

  <section class="card card--brand">
    <div class="brand-lockup">
      <span class="brand-dot"></span>
      <p class="brand-name">T Olwen<br>Plumbing &amp; Heating</p>
    </div>
  </section>

</main>
</body>
</html>
```